www.plinkro.com.au Product Catalogue

I require the design of a product catalogue to promote the products that I provide.

Sizing: A5 booklet or DL size folded brochure double sided(A4)

The catalogue will be used to promote a range of tours & adventure activities.

The catalogue needs to use high gloss full color and be like a Travel brochure.

The company name is www.plinkro.com.au

"We are the Shoalhaven' Adventure Booking Store"

Contact: info@plinkro.com.au

I have a logo which I wish to use on the front of the brochure and through out.

the website address is www.plinkro.com.au
We provide Tours & Adventure Activities in the Shoalhaven Coast region on the NSW South Coast Australia.

HERE IS A LIST OF THE TYPES OF PRODUCTS.

BOAT HIRE
COACH TOUR
TEMPLE TOUR
KANGAROO VALLEY TOUR
WINERY TOUR
FOOD & WINE TOUR
SHOALHAVEN SCENIC SIGHTS TOUR
JERVIS BAY DAY TOUR
GRAND PACIFIC DRIVE TOUR
ABORIGINAL CULTURE EXPERIENCE
VORTANE TOUR
SAILING CRUISE
RIVER CRUISE
WHALE/DOLPHIN CRUISE
SCENIC FLIGHT
SKYDIVING
WAKEBOARDING/TUBING/WATERSKIING
PADDLE BOARDING
LEARN TO SURF
KAYAKING KANGAROO VALLEY
MUSEUM
HISTORICAL SOCIETY TOURS
GHOST WALK
TREKKING
BUSH WALKING
ROCK CLIMBING
FISHING CHARTERS

We provide Online, Retail booking services as well as Gift Certificates/Vouchers.
Updates

Target Market(s)

Families, Couples, Budget Traveler

Industry/Entity Type

It Company

Font styles to use
Serif

Requirements
Must have
• Each product must have atleast 1 image.
• Please note that some of the images may be duplicates, so all I require will be the use of the image once.. not every image. Not all images are required or suitable for use, which I undestand. If you require any additional images please message me and I will see if I can provide something better for the brochure.

```html
<!DOCTYPE html>
<html lang="en">
<head>
<meta charset="utf-8">
<title>plinkro – Brochure Cover Spread</title>
<link rel="stylesheet" href="https://fonts.googleapis.com/css2?family=EB+Garamond:wght@400;700&display=swap">
<style>
  :root {
    --backdrop: #2b2b2b;
    --paper-light: #ffffff;
    --paper-shade: #d9d9d9;
    --ink: #111111;
    --ink-soft: #333333;
    --sea-deep: #0d3f8a;
    --sea-bright: #2fc0c8;
    --sky: #7fb3ea;
    --stone: #b0804a;
    --leaf: #5c7d3a;
    --sky-pale: #bcdaf2;
    --black-shape: #000000;
  }
  html, body {
    margin: 0;
    padding: 0;
    width: 1200px;
    height: 1085px;
    overflow: hidden;
    background: var(--backdrop);
    font-family: "EB Garamond", Georgia, serif;
  }
  .spread {
    position: absolute;
    left: 80px;
    top: 175px;
    width: 1040px;
    height: 735px;
    display: flex;
    box-shadow: 0 20px 50px rgba(0,0,0,0.5);
  }
  .page {
    position: relative;
    width: 520px;
    height: 735px;
    overflow: hidden;
  }
  .page--back {
    background: linear-gradient(135deg, var(--paper-shade) 0%, var(--paper-light) 45%, var(--paper-light) 70%, var(--paper-shade) 100%);
  }
  .page--front {
    background: linear-gradient(160deg, var(--paper-light) 0%, var(--paper-light) 55%, var(--paper-shade) 100%);
  }
  .page svg.shapes {
    position: absolute;
    inset: 0;
  }
  .brand-name {
    font-weight: 700;
    color: var(--ink);
    letter-spacing: 1px;
    display: flex;
    align-items: center;
    gap: 8px;
  }
  .brand-dot {
    width: 12px;
    height: 12px;
    border-radius: 50%;
    background: var(--ink);
  }
  .back-brand {
    position: absolute;
    left: 42px;
    top: 612px;
    font-size: 34px;
  }
  .contact-list {
    position: absolute;
    left: 42px;
    top: 660px;
    margin: 0;
    padding: 0;
    list-style: none;
    font-size: 15px;
    color: var(--ink-soft);
    line-height: 20px;
  }
  .contact-list li {
    display: flex;
    align-items: center;
    gap: 8px;
  }
  .contact-list svg { width: 11px; height: 11px; }
  .front-brand {
    position: absolute;
    left: 268px;
    top: 58px;
    font-size: 50px;
  }
  .front-brand .brand-dot { width: 16px; height: 16px; }
  .tagline {
    position: absolute;
    left: 268px;
    top: 132px;
    width: 210px;
    margin: 0;
    text-align: center;
    font-size: 21px;
    line-height: 26px;
    font-weight: 400;
    color: var(--ink);
  }
</style>
</head>
<body>
  <div class="spread">
    <section class="page page--back">
      <svg class="shapes" width="520" height="735" viewBox="0 0 520 735">
        <defs>
          <linearGradient id="bridgeTones" x1="0" y1="0" x2="1" y2="1">
            <stop offset="0" stop-color="var(--sky)"/>
            <stop offset="0.45" stop-color="var(--stone)"/>
            <stop offset="1" stop-color="var(--leaf)"/>
          </linearGradient>
        </defs>
        <polygon points="150,465 520,395 520,600" fill="url(#bridgeTones)" role="img" aria-label="Historic sandstone suspension bridge with castle towers"/>
        <polygon points="300,600 520,720 310,735" fill="var(--black-shape)"/>
      </svg>
      <div class="brand-name back-brand"><span class="brand-dot"></span>plinkro</div>
      <ul class="contact-list">
        <li><svg viewBox="0 0 10 10"><path d="M2 1 L4 3 L3 4 Q4.5 6 6 7 L7 6 L9 8 L7.5 9.5 Q1 8 0.5 2.5 Z" fill="var(--ink)"/></svg>02 - 4410 2273</li>
        <li><svg viewBox="0 0 10 10"><rect x="0.5" y="2" width="9" height="6" fill="var(--ink)"/><path d="M0.5 2 L5 5.5 L9.5 2" stroke="#fff" fill="none" stroke-width="0.8"/></svg>info@plinkro.com.au</li>
        <li><svg viewBox="0 0 10 10"><circle cx="5" cy="5" r="4.5" fill="var(--ink)"/><path d="M0.5 5 H9.5 M5 0.5 V9.5" stroke="#fff" stroke-width="0.7"/></svg>www.plinkro.com.au</li>
      </ul>
    </section>
    <section class="page page--front">
      <svg class="shapes" width="520" height="735" viewBox="0 0 520 735">
        <defs>
          <linearGradient id="coastTones" x1="0" y1="0" x2="0" y2="1">
            <stop offset="0" stop-color="var(--sky)"/>
            <stop offset="0.22" stop-color="var(--sky-pale)"/>
            <stop offset="0.26" stop-color="var(--leaf)"/>
            <stop offset="0.32" stop-color="var(--sea-deep)"/>
            <stop offset="0.55" stop-color="var(--sea-bright)"/>
            <stop offset="0.75" stop-color="var(--stone)"/>
            <stop offset="1" stop-color="#6f6248"/>
          </linearGradient>
          <linearGradient id="skyTones" x1="0" y1="0" x2="1" y2="1">
            <stop offset="0" stop-color="#3a86c4"/>
            <stop offset="0.5" stop-color="#c8452f"/>
            <stop offset="1" stop-color="#24607c"/>
          </linearGradient>
          <linearGradient id="trekTones" x1="0" y1="0" x2="0" y2="1">
            <stop offset="0" stop-color="var(--sky-pale)"/>
            <stop offset="0.5" stop-color="#4d7fb0"/>
            <stop offset="1" stop-color="#8a7a4c"/>
          </linearGradient>
        </defs>
        <polygon points="0,0 230,0 260,735 0,735" fill="url(#coastTones)" role="img" aria-label="Turquoise bay framed by rocky headland and bushland"/>
        <polygon points="90,470 300,690 90,735" fill="#ffffff"/>
        <polygon points="100,488 285,680 100,722" fill="url(#skyTones)" role="img" aria-label="Tandem skydivers in free fall above the coast"/>
        <polygon points="300,290 300,690 490,470" fill="url(#trekTones)" role="img" aria-label="Hikers with backpacks walking toward the sun"/>
      </svg>
      <div class="brand-name front-brand"><span class="brand-dot"></span>plinkro</div>
      <h1 class="tagline">The Shoalhaven' Adventure Booking Store</h1>
    </section>
  </div>
</body>
</html>
```